Business Card Design for Occupational Medicine Start Up Company

We need to design a professional business card. We are a healthcare company providing occupational medicine services to blue collar industries. We are professional, efficient and high quality service providers.

Target Market(s)

Blue Collar Industry: Shipbuilding, Ports, Trucking Companies; The Executives and Safety Officers for these companies

Industry/Entity Type

Healthcare

Contact Information for Business Card

Logo, Name, Title, Email, Phone

Other font styles liked:
• Please match our Brand Guide

Requirements
Must have
• Our Company Colors and Logo

```html
<!DOCTYPE html>
<html lang="en">
<head>
<meta charset="utf-8">
<title>ShiftWell Clinics – Business Card</title>
<link rel="stylesheet" href="https://fonts.googleapis.com/css2?family=Source+Sans+3:wght@400;700;800&display=swap">
<style>
  :root {
    --navy: #2b3585;
    --sky: #2f9ad8;
    --amber: #f7b24a;
    --ink: #4a4a4f;
    --rule: #6d6f78;
    --card: #ecedef;
    --backdrop: #2a2a2c;
    --font: "Source Sans 3", "Helvetica Neue", Arial, sans-serif;
  }
  * { margin: 0; padding: 0; box-sizing: border-box; }
  html, body {
    width: 1200px; height: 1107px; overflow: hidden;
    background: var(--backdrop);
    font-family: var(--font);
  }
  .canvas { position: relative; width: 1200px; height: 1107px; }

  .card {
    position: absolute;
    width: 802px; height: 462px;
    background: var(--card);
    box-shadow: 0 6px 18px rgba(0,0,0,.45);
    overflow: hidden;
  }
  .card--front { left: 239px; top: 69px; }
  .card--back  { left: 237px; top: 578px; }

  .edge-stripes { position: absolute; top: 0; bottom: 0; width: 10px; display: flex; }
  .edge-stripes span { flex: 1; }
  .edge-stripes .s-amber { background: var(--amber); }
  .edge-stripes .s-sky { background: var(--sky); }
  .edge-stripes .s-navy { background: var(--navy); }
  .card--front .edge-stripes { left: 0; }
  .card--back .edge-stripes { right: 0; }

  .brand {
    position: absolute;
    display: flex; align-items: center;
    color: var(--navy); font-weight: 800;
    letter-spacing: .5px; white-space: nowrap;
  }
  .brand-dot { border-radius: 50%; background: var(--navy); flex: none; }
  .card--front .brand { right: 48px; top: 110px; font-size: 24px; gap: 12px; }
  .card--front .brand-dot { width: 22px; height: 22px; }
  .card--back .brand {
    left: 0; right: 0; top: 210px; justify-content: center;
    font-size: 46px; gap: 20px;
  }
  .card--back .brand-dot { width: 40px; height: 40px; }

  .person { position: absolute; left: 44px; top: 215px; }
  .person-name { font-size: 27px; font-weight: 400; color: var(--navy); line-height: 1; }
  .person-name .last { color: var(--amber); }
  .person-title { margin-top: 10px; font-size: 16px; color: var(--ink); }
  .name-rule {
    position: absolute; left: 134px; width: 620px; top: 265px;
    height: 1px; background: var(--rule);
  }

  .contact-list { position: absolute; left: 44px; top: 342px; list-style: none; }
  .contact-list li {
    display: flex; align-items: center; gap: 14px;
    font-size: 17px; color: var(--ink); height: 27px;
  }
  .contact-list svg { width: 15px; height: 15px; fill: var(--navy); flex: none; }
  .contact-list .web-accent { color: var(--amber); }

  .address {
    position: absolute; right: 48px; top: 362px;
    text-align: right; font-size: 17px; line-height: 27px; color: var(--ink);
  }
</style>
</head>
<body>
<main class="canvas">

  <section class="card card--front" aria-label="Business card front">
    <div class="edge-stripes"><span class="s-sky"></span><span class="s-amber"></span><span class="s-sky"></span></div>

    <div class="brand"><span class="brand-dot"></span>SHIFTWELL CLINICS</div>

    <div class="person">
      <p class="person-name">Nadia <span class="last">Verhoef</span></p>
      <p class="person-title">Directeur</p>
    </div>
    <div class="name-rule"></div>

    <ul class="contact-list">
      <li>
        <svg viewBox="0 0 24 24" aria-hidden="true"><path d="M6.6 10.8a15.1 15.1 0 0 0 6.6 6.6l2.2-2.2a1 1 0 0 1 1-.25 11.4 11.4 0 0 0 3.6.57 1 1 0 0 1 1 1V20a1 1 0 0 1-1 1A17 17 0 0 1 3 4a1 1 0 0 1 1-1h3.5a1 1 0 0 1 1 1c0 1.25.2 2.45.57 3.57a1 1 0 0 1-.25 1z"/></svg>
        +1 780 555 0148
      </li>
      <li>
        <svg viewBox="0 0 24 24" aria-hidden="true"><path d="M2 5h20v14H2zM4 7v.5l8 5 8-5V7l-8 5z"/></svg>
        n.verhoef@shiftwell.ca
      </li>
      <li>
        <svg viewBox="0 0 24 24" aria-hidden="true"><path d="M12 2a10 10 0 1 0 0 20 10 10 0 0 0 0-20zm0 2a8 8 0 0 1 7.4 5H15a12 12 0 0 0-1.6-4.9A8 8 0 0 1 12 4zm-2 .2A12 12 0 0 0 9 9H4.6A8 8 0 0 1 10 4.2zM4.1 11h4.8a14 14 0 0 0 0 2H4.1a8 8 0 0 1 0-2zm.5 4H9a12 12 0 0 0 1.5 4.8A8 8 0 0 1 4.6 15zm6.4-4h2v2h-2zm4 4h4.4a8 8 0 0 1-5.8 4.8A12 12 0 0 0 15 15zm.1-4h4.8a8 8 0 0 1 0 2h-4.8a14 14 0 0 0 0-2z"/></svg>
        <span>www.<span class="web-accent">shiftwellclinic</span>.ca</span>
      </li>
    </ul>

    <address class="address" style="font-style:normal">
      PO BOX 5580 Elmridge<br>
      Calgary, AB T2X-4K
    </address>
  </section>

  <section class="card card--back" aria-label="Business card back">
    <div class="edge-stripes"><span class="s-navy"></span><span class="s-amber"></span><span class="s-sky"></span></div>
    <div class="brand"><span class="brand-dot"></span>SHIFTWELL CLINICS</div>
  </section>

</main>
</body>
</html>
```